Realty Group Needs Classy, Contemporary Letterhead Design

We need a letterhead design for a new realty company located in NY, USA. We buy investment properties to rehabilitate and or keep in our rental portfolio.

```html
<!DOCTYPE html>
<html lang="en">
<head>
<meta charset="utf-8">
<title>Meridian Realty Group — Letterhead</title>
<link href="https://fonts.googleapis.com/css2?family=Montserrat:wght@600;800&family=PT+Sans:wght@700&display=swap" rel="stylesheet">
<style>
  :root {
    --backdrop: #dcdcdc;
    --paper: #ffffff;
    --brand-purple: #4f2d83;
    --brand-grey: #a3a3a1;
    --tagline-grey: #6f6f6f;
    --body-grey: #c4c4c4;
    --ghost-grey: #d7d7d6;
    --shadow-dark: #3c3c3c;
  }
  * { margin: 0; padding: 0; box-sizing: border-box; }
  html, body { width: 1200px; height: 762px; overflow: hidden; background: var(--backdrop); }
  .canvas { position: relative; width: 1200px; height: 762px; }

  .sheet {
    position: absolute;
    width: 440px;
    height: 570px;
    background: var(--paper);
    overflow: hidden;
    box-shadow:
      6px 6px 0 0 #cfcfcf,
      12px 10px 8px 2px rgba(0,0,0,.45),
      20px 14px 16px 4px rgba(0,0,0,.25);
  }
  .sheet--blank { left: 96px; top: 97px; }
  .sheet--letter { left: 646px; top: 98px; }

  .brand { position: absolute; left: 22px; top: 30px; }
  .brand__name {
    font-family: "Montserrat", sans-serif;
    font-weight: 800;
    font-size: 27px;
    line-height: 1;
    letter-spacing: -0.5px;
    color: var(--brand-purple);
  }
  .brand__tagline {
    margin: 3px 0 0 34px;
    font-family: "Montserrat", sans-serif;
    font-weight: 600;
    font-size: 8.5px;
    letter-spacing: 0.6px;
    color: var(--tagline-grey);
  }

  .header-bars { position: absolute; left: 0; top: 0; width: 440px; height: 100px; }
  .header-bars .bar--purple { fill: var(--brand-purple); }
  .header-bars .bar--grey { fill: var(--brand-grey); }

  .letter-body {
    position: absolute;
    left: 40px;
    top: 161px;
    width: 370px;
    font-family: "PT Sans", sans-serif;
    font-weight: 700;
  }
  .letter-body__heading {
    font-size: 11.5px;
    color: var(--brand-purple);
    margin: 0 0 11px 2px;
  }
  .letter-body__para {
    font-size: 7.8px;
    line-height: 10.4px;
    color: var(--body-grey);
    margin-bottom: 11px;
  }

  .sign-off { position: absolute; left: 315px; top: 320px; width: 80px; }
  .sign-off__name {
    font-family: "PT Sans", sans-serif;
    font-weight: 700;
    font-size: 6px;
    color: #9a9a9a;
    margin-left: 25px;
  }
  .sign-off__signature {
    margin-top: 3px;
    width: 80px;
    height: 14px;
    background: linear-gradient(90deg, #e2e2e2, #cfcfcf, #e2e2e2);
    border-radius: 2px;
  }

  .ghost-mark { position: absolute; left: 0; bottom: 0; width: 440px; height: 60px; }
  .ghost-mark text {
    font-family: "Montserrat", sans-serif;
    font-weight: 800;
    font-size: 66px;
    fill: var(--ghost-grey);
  }
</style>
</head>
<body>
<main class="canvas">

  <section class="sheet sheet--blank" aria-label="Blank letterhead">
    <div class="brand">
      <div class="brand__name">MERIDIAN</div>
      <div class="brand__tagline">Realty Group, LLC</div>
    </div>
    <svg class="header-bars" viewBox="0 0 440 100" aria-hidden="true">
      <polygon class="bar--purple" points="22,72 284,72 291,80 22,80"/>
      <polygon class="bar--grey" points="137,82 291,82 290,80 290,76 406,76 413,85 137,85"/>
    </svg>
    <svg class="ghost-mark" viewBox="0 0 440 60" aria-hidden="true">
      <text x="0" y="59" textLength="440" lengthAdjust="spacingAndGlyphs">MERIDIAN</text>
    </svg>
  </section>

  <section class="sheet sheet--letter" aria-label="Letterhead with sample letter">
    <div class="brand">
      <div class="brand__name">MERIDIAN</div>
      <div class="brand__tagline">Realty Group, LLC</div>
    </div>
    <svg class="header-bars" viewBox="0 0 440 100" aria-hidden="true">
      <polygon class="bar--purple" points="27,74 289,74 296,82 27,82"/>
      <polygon class="bar--grey" points="142,84 296,84 295,82 295,78 411,78 418,87 142,87"/>
    </svg>

    <article class="letter-body">
      <h2 class="letter-body__heading">Realty Group</h2>
      <p class="letter-body__para">Real estate company introduction letter is the most cost-effective method you can use to introduce your company. Prospects in general, don’t wish to work with the company which has no exposure. So it is important that the prospect knows your company and has been receiving your messages often. In real estate, in order to develop regular communication with your potential prospect, it is vital that you get an excellent head start over your competitors.</p>
      <p class="letter-body__para">Real estate company introduction letter is the most cost-effective method you can use to introduce your company. Prospects in general, don’t wish to work with the company which has no exposure. So it is important that the prospect knows your company and has been receiving your messages often. In real estate, in order to develop regular communication with your potential prospect, it is vital that you get an excellent head start over your competitors.</p>
    </article>

    <div class="sign-off">
      <div class="sign-off__name">Realty Group</div>
      <div class="sign-off__signature" role="img" aria-label="Handwritten signature"></div>
    </div>

    <svg class="ghost-mark" viewBox="0 0 440 60" aria-hidden="true">
      <text x="0" y="59" textLength="440" lengthAdjust="spacingAndGlyphs">MERIDIAN</text>
    </svg>
  </section>

</main>
</body>
</html>
```